Halvercott Orthodontics business card

Using our existing logo (created with ArtFolio), please create a tasteful, contemporary business card. We are father and daughter orthodontists specializing in braces, clarafit, etc to design healthy, beautiful smiles for children, adolescents, and adults. We would like the design to be family-friendly but not childish.
The final design should include all of the information without looking cluttered (I hope! If necessary to achieve an optimal design, please consider making the card double-sided)
Purple, black, silver on a white card
Please include the following information:
Halvercott Orthodontics (logo)
Marguerite L. Halvercott, DMD
Douglas R. Halvercott, DMD

312 Bramblewood Street
North Andover, MA 01899
978.555.0142

847C Quarry Hollow Street
Methuen, MA 01898
978.555.0187

email frontdesk@halvercottortho.example
website www.halvercottortho.example

```html
<!DOCTYPE html>
<html lang="en">
<head>
<meta charset="utf-8">
<title>Halvercott Orthodontics — Business Card</title>
<link rel="stylesheet" href="https://fonts.googleapis.com/css2?family=Source+Sans+3:wght@400;600;700&display=swap">
<style>
  :root {
    --backdrop: #d9d9d9;
    --brand-purple: #663493;
    --card-white: #ffffff;
    --ink-white: #ffffff;
    --ink-dark: #3a3a3a;
    --silver: #8a8a8a;
  }
  html, body {
    margin: 0;
    padding: 0;
    width: 1200px;
    height: 1200px;
    overflow: hidden;
    background: var(--backdrop);
    font-family: "Source Sans 3", "Source Sans Pro", Arial, sans-serif;
  }
  .canvas {
    position: relative;
    width: 1200px;
    height: 1200px;
  }
  .card {
    position: absolute;
    width: 661px;
    height: 376px;
    border-radius: 15px;
    overflow: hidden;
  }
  .card--front {
    left: 120px;
    top: 155px;
    background: var(--brand-purple);
    color: var(--ink-white);
  }
  .card--back {
    left: 410px;
    top: 684px;
    background: var(--card-white);
  }
  .brand {
    position: absolute;
    left: 0;
    right: 0;
    display: flex;
    align-items: center;
    justify-content: center;
    gap: 14px;
    font-weight: 600;
    font-size: 36px;
    letter-spacing: 0.5px;
    white-space: nowrap;
  }
  .card--front .brand { top: 82px; color: var(--ink-white); }
  .card--back .brand { top: 120px; color: var(--brand-purple); }
  .brand__dot {
    width: 22px;
    height: 22px;
    border-radius: 50%;
    background: currentColor;
    flex: none;
  }
  .doctors {
    position: absolute;
    left: 14px;
    top: 212px;
    margin: 0;
  }
  .doctor {
    margin: 0 0 8px;
    font-weight: 700;
    font-size: 23px;
    line-height: 29px;
  }
  .contact {
    position: absolute;
    left: 359px;
    top: 216px;
    margin: 0;
    padding: 0;
    list-style: none;
    font-weight: 600;
    font-size: 14px;
    line-height: 19px;
  }
  .contact__item {
    display: flex;
    align-items: center;
    gap: 12px;
    margin-bottom: 9px;
  }
  .contact__icon {
    width: 20px;
    height: 20px;
    flex: none;
    fill: var(--ink-white);
  }
  .accent-rule {
    position: absolute;
    left: 346px;
    top: 347px;
    width: 315px;
    height: 6px;
  }
  .offices {
    position: absolute;
    left: 0;
    right: 0;
    top: 215px;
    display: flex;
    justify-content: center;
    gap: 70px;
  }
  .office {
    text-align: center;
    font-size: 15px;
    line-height: 21px;
    color: var(--ink-dark);
  }
  .office__name {
    margin: 0 0 4px;
    font-weight: 700;
    font-size: 13px;
    letter-spacing: 2px;
    text-transform: uppercase;
    color: var(--brand-purple);
  }
  .office__line { margin: 0; }
  .office__phone { margin: 2px 0 0; font-weight: 600; color: var(--silver); }
</style>
</head>
<body>
<main class="canvas">

  <section class="card card--front" aria-label="Business card front">
    <div class="brand"><span class="brand__dot"></span>Halvercott Orthodontics</div>

    <div class="doctors">
      <p class="doctor">Marguerite L. Halvercott<br>DMD</p>
      <p class="doctor">Douglas R. Halvercott<br>DMD</p>
    </div>

    <ul class="contact">
      <li class="contact__item">
        <svg class="contact__icon" viewBox="0 0 24 24" aria-hidden="true"><path d="M6.6 10.8a15.1 15.1 0 0 0 6.6 6.6l2.2-2.2a1 1 0 0 1 1-.25 11.4 11.4 0 0 0 3.6.57 1 1 0 0 1 1 1V20a1 1 0 0 1-1 1A17 17 0 0 1 3 4a1 1 0 0 1 1-1h3.5a1 1 0 0 1 1 1c0 1.25.2 2.45.57 3.57a1 1 0 0 1-.25 1z"/></svg>
        <span>978-555-0142</span>
      </li>
      <li class="contact__item">
        <svg class="contact__icon" viewBox="0 0 24 24" aria-hidden="true"><path d="M12 3 2 12h3v9h5v-6h4v6h5v-9h3z"/></svg>
        <span>312 Bramblewood Street, North Andover<br>MA 01899</span>
      </li>
      <li class="contact__item">
        <svg class="contact__icon" viewBox="0 0 24 24" aria-hidden="true"><path d="M2 5h20v14H2zm2 2v.4l8 6 8-6V7zm0 2.9V17h16V9.9l-8 6z"/></svg>
        <span>frontdesk@halvercottortho.example</span>
      </li>
      <li class="contact__item">
        <svg class="contact__icon" viewBox="0 0 24 24" aria-hidden="true"><path d="M12 2a10 10 0 1 0 0 20 10 10 0 0 0 0-20zm1 2.1c1.3.9 2.3 2.9 2.7 5.4H13zm-2 0v5.4H8.3c.4-2.5 1.4-4.5 2.7-5.4zM4.1 11.5h4c0 .3-.1.7-.1 1s0 .3.1.5h-4a8 8 0 0 1 0-1.5zm6.9 0v1.5H8.1a7 7 0 0 1 0-1.5zm2 0h2.9a7 7 0 0 1 0 1.5H13zm4.9 0h4a8 8 0 0 1 0 1.5h-4a9 9 0 0 0 0-1.5zM8.3 15H11v4.9c-1.3-.9-2.3-2.6-2.7-4.9zm4.7 0h2.7c-.4 2.3-1.4 4-2.7 4.9z"/></svg>
        <span>www.halvercottortho.example</span>
      </li>
    </ul>

    <svg class="accent-rule" viewBox="0 0 315 6" preserveAspectRatio="none" aria-hidden="true">
      <polygon points="0,0 315,0 315,6 6,6" fill="#ffffff"/>
    </svg>
  </section>

  <section class="card card--back" aria-label="Business card back">
    <div class="brand"><span class="brand__dot"></span>Halvercott Orthodontics</div>

    <div class="offices">
      <div class="office">
        <p class="office__name">North Andover</p>
        <p class="office__line">312 Bramblewood Street</p>
        <p class="office__line">North Andover, MA 01899</p>
        <p class="office__phone">978-555-0142</p>
      </div>
      <div class="office">
        <p class="office__name">Methuen</p>
        <p class="office__line">847C Quarry Hollow Street</p>
        <p class="office__line">Methuen, MA 01898</p>
        <p class="office__phone">978-555-0187</p>
      </div>
    </div>
  </section>

</main>
</body>
</html>
```